Letterhead for invoices and engagement letter

Want to use logos sourced on quillorbit to create letterhead templates for word or pdf files

Industry/Entity Type

Legal- law firm

Colors
0054AA
0677BA
7BADD7
CADEEF
E8F1F8

```html
<!DOCTYPE html>
<html lang="en">
<head>
<meta charset="utf-8">
<title>The Harlow Firm – Letterhead</title>
<link href="https://fonts.googleapis.com/css2?family=Questrial&display=swap" rel="stylesheet">
<style>
  :root {
    --backdrop: #e9e9eb;
    --paper: #ffffff;
    --ink-navy: #15233d;
    --ink-body: #3a3a3c;
    --ink-muted: #555a63;
    --watermark: #eceef1;
    --signature-tone: #e4e6ea;
  }
  * { box-sizing: border-box; margin: 0; padding: 0; }
  html, body {
    width: 1200px; height: 960px; overflow: hidden;
    background: var(--backdrop);
  }
  .letterhead {
    position: absolute; left: 252px; top: 30px;
    width: 696px; height: 900px;
    background: var(--paper);
    overflow: hidden;
    box-shadow: 0 2px 6px rgba(0,0,0,0.08);
  }
  .brand {
    position: absolute; left: 46px; top: 50px;
    display: flex; align-items: center; gap: 14px;
  }
  .brand-dot {
    width: 58px; height: 58px; border-radius: 50%;
    background: var(--ink-navy);
  }
  .brand-name {
    font-family: "Questrial", sans-serif;
    color: var(--ink-navy);
    font-size: 20px; line-height: 1.05; letter-spacing: 2px;
    text-transform: uppercase;
  }
  .contact {
    position: absolute; left: 470px; top: 48px;
    border-left: 1px solid var(--ink-navy);
    padding-left: 12px;
    font-family: Arial, Helvetica, sans-serif;
    font-size: 10.5px; line-height: 1.3; color: var(--ink-muted);
    list-style: none;
  }
  .contact li { display: flex; align-items: flex-start; gap: 6px; }
  .contact svg { width: 9px; height: 9px; margin-top: 2px; flex: none; fill: var(--ink-navy); }
  .watermark {
    position: absolute; left: 470px; top: 330px;
    width: 330px; height: 330px; border-radius: 50%;
    background: var(--watermark);
  }
  .letter {
    position: relative;
    padding: 300px 120px 0 112px;
    font-family: Arial, Helvetica, sans-serif;
    color: var(--ink-body);
  }
  .salutation {
    font-family: "Questrial", sans-serif;
    font-weight: 700; font-size: 16px; color: var(--ink-body);
    margin-bottom: 14px;
  }
  .letter p.body-copy {
    font-size: 12px; line-height: 1.32; margin-bottom: 15px;
    padding-left: 12px;
  }
  .closing {
    font-size: 10px; font-weight: 700; margin-top: 22px; padding-left: 46px;
  }
  .signature {
    width: 120px; height: 36px; margin: 14px 0 0 78px;
    background: var(--signature-tone); border-radius: 4px;
  }
</style>
</head>
<body>
  <main class="letterhead">
    <header>
      <div class="brand">
        <span class="brand-dot"></span>
        <div class="brand-name">The<br>Harlow<br>Firm PLC</div>
      </div>
      <ul class="contact">
        <li>
          <svg viewBox="0 0 10 10"><path d="M5 0a3.5 3.5 0 0 0-3.5 3.5C1.5 6 5 10 5 10s3.5-4 3.5-6.5A3.5 3.5 0 0 0 5 0zm0 5a1.5 1.5 0 1 1 0-3 1.5 1.5 0 0 1 0 3z"/></svg>
          <span>Your address, city<br>state, ZIP 0000</span>
        </li>
        <li>
          <svg viewBox="0 0 10 10"><path d="M2 0.5l2 2-1 1.2a6 6 0 0 0 3.3 3.3l1.2-1 2 2-1.3 1.5C4.5 9.5 0.5 5.5 0.5 1.8z"/></svg>
          <span>123-456-2100</span>
        </li>
        <li>
          <svg viewBox="0 0 10 10"><path d="M0 2h10v6H0z M0 2l5 3.5L10 2" fill="none" stroke="#15233d" stroke-width="1.2"/></svg>
          <span>youremail@mailpost.com</span>
        </li>
        <li>
          <svg viewBox="0 0 10 10"><circle cx="5" cy="5" r="4.3" fill="none" stroke="#15233d" stroke-width="1.2"/><path d="M1 5h8M5 0.7c-2 2.6-2 6 0 8.6M5 0.7c2 2.6 2 6 0 8.6" fill="none" stroke="#15233d" stroke-width="0.9"/></svg>
          <span>www.yourwebsite.com</span>
        </li>
      </ul>
    </header>

    <div class="watermark" aria-hidden="true"></div>

    <section class="letter">
      <p class="salutation">Dear Mr. Ellery,</p>
      <p class="body-copy">Lorem ipsum dolor sit amet, consectetuer adipiscing elit, sed diam nonummy nibh euismod tincidunt ut laoreet dolore magna aliquam erat volutpat. Ut wisi enim ad minim veniam, quis nostrud exerci tationmcorper suscipit lobortis nisl ut aliquip ex ea commodo consequat. Duis autem vel eum iriure dolor in hendrerit in vulputate velit esse molestie consequat, vel illum dolore eu feugiat</p>
      <p class="body-copy">Rorem ipsum dolor sit amet, consectetuer adipiscing elit, sed diam nonummy nibh euismod tincidunt ut laoreet dolore magna aliquam erat volutpat. Ut wisi enim ad minim veniam, quis nostrud exerci tationmcorper suscipit lobortis nisl ut aliquip ex ea commodo consequat. Duis autem vel eum iriure dolor in hendrerit in vulputate velit esse molest</p>
      <p class="body-copy">Dorem ipsum dolor sit amet, consectetuer adipiscing elit, sed diam nonummy nibh euismod tincidunt ut laoreet dolore magna aliquam erat volutpat. Ut wisi enim ad minim veniam, quis nostrud exerci tationmcorper suscipit lobortis nisl ut aliquip ex ea commodo consequat. Duis autem vel eum iriure dolor in hendrerit in vulputate velit esse molestie consequat, vel illum</p>
      <p class="body-copy">Sorem ipsum dolor sit amet, consectetuer adipiscing elit, sed diam nonummy nibh euismod tincidunt ut laoreet dolore magna aliquam erat volutpat. Ut wisi enim ad minim veniam, quis nostrud exerci tationmcorper suscipit lobortis nisl ut aliquip ex ea commodo consequat. Duis autem vel eum iriure dolor in</p>
      <p class="closing">Sincerely,</p>
      <div class="signature" role="img" aria-label="Handwritten signature of the sender"></div>
    </section>
  </main>
</body>
</html>
```